Business Card Design

New business card design

Target Market(s)

Residential & Commercial Property Managers

Industry/Entity Type

Plumbing Services

Contact Information for Business Card

Name - Owen Tredgold, title - Director, Phone Number - 0431 862 507, email - owen@rvb-plumbing.com.au, Company ABN - 73 215 904 386,

Font styles to use
Sans Serif

Colors
0054AA
0677BA
7BADD7
CADEEF
E8F1F8

```html
<!DOCTYPE html>
<html lang="en">
<head>
<meta charset="utf-8">
<title>RVB Plumbing Services – Business Card</title>
<link href="https://fonts.googleapis.com/css2?family=Arimo:wght@400;700&display=swap" rel="stylesheet">
<style>
  :root {
    --backdrop: #9a9a9a;
    --card-white: #fbfbfb;
    --card-navy: #0e1326;
    --ink: #333840;
    --ink-soft: #55595f;
    --accent: #29a9e6;
    --white: #ffffff;
  }
  * { margin: 0; padding: 0; box-sizing: border-box; }
  html, body {
    width: 1200px;
    height: 1050px;
    overflow: hidden;
    background: var(--backdrop);
    font-family: "Arimo", Arial, sans-serif;
  }
  .canvas {
    position: relative;
    width: 1200px;
    height: 1050px;
  }
  .card {
    position: absolute;
    left: 300px;
    width: 600px;
    height: 343px;
    border-radius: 22px;
    overflow: hidden;
    box-shadow: 0 10px 26px rgba(0,0,0,0.22);
  }
  .card--front { top: 150px; background: var(--card-white); }
  .card--back  { top: 557px; background: var(--card-navy); }

  /* Front: contact column set vertically, reading upward */
  .contact-column {
    position: absolute;
    left: 50%;
    top: 50%;
    width: 290px;
    transform: translate(-50%, -50%) rotate(-90deg);
    color: var(--ink);
  }
  .front-brand {
    font-size: 17px;
    font-weight: 400;
    color: var(--ink);
    letter-spacing: 0.5px;
    margin-bottom: 26px;
  }
  .person-name {
    font-size: 26px;
    font-weight: 700;
    line-height: 1;
  }
  .person-title {
    font-size: 15px;
    color: var(--accent);
    margin-top: 2px;
    margin-bottom: 22px;
  }
  .contact-line {
    font-size: 15px;
    color: var(--ink-soft);
    line-height: 1.5;
  }
  .contact-line--gap { margin-bottom: 16px; }

  /* Back: company name */
  .back-brand {
    position: absolute;
    inset: 0;
    display: flex;
    align-items: center;
    justify-content: center;
    color: var(--white);
    font-size: 40px;
    font-weight: 400;
    letter-spacing: 2px;
    padding-bottom: 20px;
  }
</style>
</head>
<body>
<main class="canvas">
  <section class="card card--front" aria-label="Business card front">
    <div class="contact-column">
      <p class="front-brand">RVB Plumbing Services</p>
      <p class="person-name">Owen Tredgold</p>
      <p class="person-title">Director</p>
      <p class="contact-line contact-line--gap">ABN - 73 215 904 386</p>
      <p class="contact-line">0431 862 507</p>
      <p class="contact-line">owen@rvb-plumbing.com.au</p>
    </div>
  </section>

  <section class="card card--back" aria-label="Business card back">
    <p class="back-brand">RVB Plumbing Services</p>
  </section>
</main>
</body>
</html>
```